Packaging Design Project for Snack product

we are manufacturer banana chips and potato based snacks.our company name is "velmora Foods" and,looking a packaging design for our new product "Potato Twirlies" under brand name " Munchlo".

we need nice colour scheme and wording on the front and back.just a little more professional looking with the wow factor to help it stand out on the shelve.

so pls find below information about the design:
Company name: Velmora Foods
Brand name : Munchlo
Product name : Potato Twirlies
Flavored : Sweet & Spicy
Package Size : 40 GM and 100 GM

Target Market(s)

Retail Customers

Industry/Entity Type

It Company

Requirements
Must have
• In this design we need small visible part for display our product.

```html
<!DOCTYPE html>
<html lang="en">
<head>
<meta charset="utf-8">
<title>Munchlo Potato Twirlies – Packaging Range</title>
<link rel="stylesheet" href="https://fonts.googleapis.com/css2?family=Archivo+Black&family=Arimo:wght@700&family=Playfair+Display:ital,wght@1,700&family=Rubik+Dirt&display=swap">
<style>
  :root {
    --stage: #e4e4e4;
    --brand-yellow: #f2ec1c;
    --company-gold: #f5c51b;
    --title-white: #ffffff;
    --flavour-band: #55c6ee;
    --flavour-ink: #0d1f3a;
    --size-ink: #ffffff;
    --teal: #2fb3d8;
    --green: #14963a;
    --green-deep: #0b6b2d;
    --red: #e01f27;
    --red-deep: #a8121a;
    --blue: #2c7bd6;
    --blue-deep: #1c4fa0;
    --plum: #b8406a;
    --chip-gold: #f0cf6a;
    --chip-light: #fbe7a2;
  }
  * { margin: 0; padding: 0; box-sizing: border-box; }
  html, body { width: 1200px; height: 614px; overflow: hidden; }
  body { background: var(--stage); position: relative; }

  .bag {
    position: absolute;
    top: 52px;
    width: 378px;
    height: 506px;
    display: flex;
    flex-direction: column;
    align-items: center;
    overflow: hidden;
  }
  .bag--green { left: 27px; background:
      radial-gradient(ellipse 70% 45% at 55% 55%, var(--teal) 0%, transparent 70%),
      linear-gradient(160deg, var(--green) 0%, var(--green-deep) 40%, var(--teal) 75%, var(--green) 100%); }
  .bag--red { left: 410px; background:
      radial-gradient(ellipse 70% 45% at 45% 55%, var(--teal) 0%, transparent 70%),
      linear-gradient(160deg, var(--red) 0%, var(--red-deep) 40%, var(--red) 70%, var(--teal) 100%); }
  .bag--blue { left: 794px; background:
      radial-gradient(ellipse 60% 40% at 75% 40%, var(--plum) 0%, transparent 70%),
      linear-gradient(160deg, var(--blue) 0%, var(--teal) 45%, var(--blue-deep) 80%, var(--blue) 100%); }

  .crimp {
    position: absolute;
    left: 0; right: 0;
    height: 14px;
    background: repeating-linear-gradient(90deg, rgba(255,255,255,0.28) 0 3px, rgba(0,0,0,0.18) 3px 6px);
  }
  .crimp--top { top: 0; }
  .crimp--bottom { bottom: 0; }

  .brand-name {
    margin-top: 20px;
    font-family: "Archivo Black", sans-serif;
    font-size: 52px;
    line-height: 1;
    color: var(--brand-yellow);
  }
  .company-name {
    margin-top: 2px;
    font-family: "Playfair Display", serif;
    font-style: italic;
    font-weight: 700;
    font-size: 28px;
    color: var(--company-gold);
  }
  .product-line {
    font-family: "Rubik Dirt", sans-serif;
    color: var(--title-white);
    line-height: 1;
    text-align: center;
  }
  .product-line--first { margin-top: 8px; font-size: 82px; }
  .product-line--second { font-size: 66px; margin-top: -4px; }

  .product-window {
    width: 260px;
    height: 96px;
    margin: 6px 0 4px;
    border-radius: 50% 46% 44% 50%;
    background: radial-gradient(ellipse at 45% 40%, var(--chip-light) 0%, var(--chip-gold) 60%, rgba(240,207,106,0.6) 100%);
  }

  .flavour-band {
    position: absolute;
    left: 0; right: 0;
    top: 412px;
    height: 52px;
    background: var(--flavour-band);
    display: flex;
    align-items: center;
    justify-content: center;
    font-family: "Arimo", sans-serif;
    font-weight: 700;
    font-size: 38px;
    color: var(--flavour-ink);
  }
  .pack-sizes {
    position: absolute;
    right: 16px;
    top: 468px;
    font-family: "Arimo", sans-serif;
    font-weight: 700;
    font-size: 18px;
    color: var(--size-ink);
  }
</style>
</head>
<body>
  <section class="bag bag--green">
    <span class="crimp crimp--top"></span>
    <h1 class="brand-name">Munchlo</h1>
    <p class="company-name">Velmora Foods</p>
    <h2 class="product-line product-line--first">POTATO</h2>
    <div class="product-window" role="img" aria-label="Window showing golden potato snacks"></div>
    <h2 class="product-line product-line--second">TWIRLIES</h2>
    <p class="flavour-band">Sweet &amp; Spicy</p>
    <p class="pack-sizes">40 GM and 100 GM</p>
    <span class="crimp crimp--bottom"></span>
  </section>

  <section class="bag bag--red">
    <span class="crimp crimp--top"></span>
    <h1 class="brand-name">Munchlo</h1>
    <p class="company-name">Velmora Foods</p>
    <h2 class="product-line product-line--first">POTATO</h2>
    <div class="product-window" role="img" aria-label="Window showing golden potato snacks"></div>
    <h2 class="product-line product-line--second">TWIRLIES</h2>
    <p class="flavour-band">Sweet &amp; Spicy</p>
    <p class="pack-sizes">40 GM and 100 GM</p>
    <span class="crimp crimp--bottom"></span>
  </section>

  <section class="bag bag--blue">
    <span class="crimp crimp--top"></span>
    <h1 class="brand-name">Munchlo</h1>
    <p class="company-name">Velmora Foods</p>
    <h2 class="product-line product-line--first">POTATO</h2>
    <div class="product-window" role="img" aria-label="Window showing golden potato snacks"></div>
    <h2 class="product-line product-line--second">TWIRLIES</h2>
    <p class="flavour-band">Sweet &amp; Spicy</p>
    <p class="pack-sizes">40 GM and 100 GM</p>
    <span class="crimp crimp--bottom"></span>
  </section>
</body>
</html>
```